R&T Architects - business card and stationary

Aloha,

We have a simple text logo, we need it incorporated into a business card and also stationary design (letterhead) if possible.

Please check out our website, rtamaui-studio.example for a little more about us. The logo we would like to use is in the upper left corner of the website. It is a simple colored logo based on the Klavica font. We are open to new logo's as well, but we want simple.

Thanks

```html
<!DOCTYPE html>
<html lang="en">
<head>
<meta charset="utf-8">
<title>R&amp;T Architects – Business Card</title>
<link rel="stylesheet" href="https://fonts.googleapis.com/css2?family=PT+Sans&family=Tinos&display=swap">
<style>
  :root {
    --backdrop: #ecebe7;
    --card: #ffffff;
    --leaf-green: #7fa63a;
    --leaf-light: #b9d27f;
    --accent-green: #6c9b26;
    --block-top: #6aa524;
    --block-bottom: #3f7a16;
    --ink-dark: #4a4630;
    --ink-contact: #3b3a30;
  }
  * { box-sizing: border-box; margin: 0; padding: 0; }
  html, body {
    width: 1200px;
    height: 947px;
    overflow: hidden;
    background: var(--backdrop);
  }
  .canvas {
    position: relative;
    width: 1200px;
    height: 947px;
  }
  .card {
    position: absolute;
    width: 740px;
    height: 440px;
    background: var(--card);
    box-shadow: 0 4px 14px rgba(0,0,0,0.18);
    overflow: hidden;
  }
  .card--front { left: 60px; top: 40px; }
  .card--back { left: 400px; top: 440px; }

  .vine-art {
    position: absolute;
    left: 0;
    top: 0;
    width: 230px;
    height: 100%;
    background: linear-gradient(100deg, var(--leaf-green) 0%, var(--leaf-light) 55%, rgba(255,255,255,0) 100%);
    opacity: 0.75;
  }

  .company-name {
    position: absolute;
    font-family: "PT Sans", sans-serif;
    font-weight: 400;
    color: var(--ink-dark);
    line-height: 1;
    white-space: nowrap;
  }
  .card--front .company-name { left: 260px; top: 190px; font-size: 54px; }
  .card--back .company-name { left: 235px; top: 130px; font-size: 50px; }

  .accent-block {
    position: absolute;
    left: 0;
    top: 160px;
    width: 155px;
    height: 200px;
    border-radius: 0 12px 12px 0;
    background: linear-gradient(180deg, var(--block-top), var(--block-bottom));
  }

  .holder-name {
    position: absolute;
    left: 237px;
    top: 255px;
    font-family: "PT Sans", sans-serif;
    font-size: 27px;
    line-height: 1.2;
    color: var(--ink-dark);
  }
  .contact {
    position: absolute;
    left: 237px;
    top: 315px;
    font-family: "Tinos", serif;
    font-size: 20px;
    line-height: 24px;
    color: var(--ink-contact);
    list-style: none;
  }
  .contact .accent { color: var(--accent-green); }
</style>
</head>
<body>
<main class="canvas">
  <section class="card card--front">
    <div class="vine-art" role="img" aria-label="Green flowing vine ornament with leaves and swirls along the left edge"></div>
    <h1 class="company-name">R&amp;T Architects</h1>
  </section>

  <section class="card card--back">
    <div class="accent-block"></div>
    <p class="company-name">R&amp;T Architects</p>
    <p class="holder-name">Leilani Kahale</p>
    <ul class="contact">
      <li>(808) <span class="accent">555-0147</span></li>
      <li>Leilani@<span class="accent">rtamaui-studio.example</span></li>
      <li>rtamaui-studio.example</li>
    </ul>
  </section>
</main>
</body>
</html>
```